New Website for IT Services Business

We need an uncoded web design for a new company based in Australia called "Falcon IT". We offer specialised point of sale (POS) support to the hospitality industry. We already support hundreds of cafes and restaurants. We are also about to launch and promote a range of new services with the offering of General IT Support being the most important. Other additional services to be offered are Falcon Vault Storage, reselling and supporting Corvel Shieldware and Trelmo Suite.

We have a logo design and our colour scheme is based on the logo with the addition of charcoal grey (see attached logos). We want the pages to reflect precision and efficiency with sharp characteristics. It must be professional but playful/fun elements are encouraged.

Our target audience is restaurant and cafe owners who are interested in finding high quality POS and IT support for their business.

The main call to action on the home page should be either 'Let's Meet For Coffee!' or 'Find out more (by completing a form)'. If you are unsure about what the general text should say then you can use 'Lorem Ipsum' where required.

The site must be viewable at different resolutions and on smart phones and tablets.

The website structure will be quite simple. We require:
- one impressive landing page. Visitors will quickly determine our services and that we provide a very high level of service while also offering value for money. Obviously a clear list of links (however/wherever you like) to the other pages.
- Simple pages with a similar layout for the following:
- Services - "POS & IT Support for the Hospitality Industry" being the main one. With complementary services also listed. Another call to action on this page with the option of 'Let's Meet For Coffee' or a "More information/Pricing" form to be completed by the visitor.
- Products - will be a small online storefront for a few simple products.
- About - Business background. 2x Directors with a photo and brief Bio.
- Downloads - A list of free files to download. Includes remote access client software.
- Contact Us - Mailing address, Email addresses and Support phone number.

Please feel free to ask any questions about the design. I will assist as much as possible.

Thank you for viewing. We promise to give constructive feedback to every person who submits a design. Thank you so much.

Target Market(s)

Restaurant and Cafe owners.

Industry/Entity Type

Hospitality

Requirements
Must have
• - Viewable on different resolutions and on smart phones and tablets.
- Clear call to action of EITHER 'Let's Meet For Coffee' or a "More information/Pricing" form to be completed by the visitor.

```html
<!DOCTYPE html>
<html lang="en">
<head>
<meta charset="utf-8">
<title>Falcon IT – POS &amp; IT Support for Hospitality</title>
<link href="https://fonts.googleapis.com/css2?family=Open+Sans:wght@400;600;700&family=Oswald:wght@400;500&family=Bree+Serif&family=Libre+Baskerville:ital@0;1&display=swap" rel="stylesheet">
<style>
:root{
  --red:#d41f30;
  --charcoal:#262626;
  --panel:#3a3a3a;
  --field:#262626;
  --text:#444;
  --muted:#777;
  --rule:#e4e4e4;
  --band:#f2f2f2;
  --partner:#9a9a9a;
  --white:#fff;
}
*{margin:0;padding:0;box-sizing:border-box}
html,body{width:719px;height:1200px;overflow:hidden;background:var(--white)}
body{position:relative;font-family:"Open Sans",Arial,sans-serif;color:var(--text)}
.abs{position:absolute}

/* header */
.site-header{left:0;top:0;width:719px;height:77px;background:linear-gradient(#fff,#e9e9e9);border-bottom:1px solid #ddd}
.brand{left:85px;top:20px;display:flex;align-items:center;gap:8px}
.brand-dot{width:40px;height:40px;border-radius:50%;background:var(--red)}
.brand-name{font-family:"Open Sans",sans-serif;font-weight:700;font-size:27px;color:var(--charcoal);letter-spacing:-.5px}
.call{right:89px;top:8px;font-family:"Oswald",sans-serif;font-size:14px;color:#333;white-space:nowrap}
.call strong{font-weight:500;color:var(--red);font-size:20px;margin-left:6px;vertical-align:-2px}
.email-line{right:89px;top:29px;font-size:6.5px;color:#555}
.email-line span{color:#1a8ad4}
.main-nav{right:85px;top:57px;display:flex;font-size:9px;font-weight:600;color:#444}
.main-nav a{color:inherit;text-decoration:none;padding:0 6px;border-left:1px solid #ccc}
.main-nav a:first-child{border-left:0}
.main-nav a:last-child{padding-right:0}

/* hero */
.hero-copy{left:84px;top:100px;width:150px;height:235px;background:var(--red);color:var(--white);padding:12px 6px}
.hero-kicker{font-size:15px;line-height:16px;font-weight:400}
.hero-title{font-family:"Oswald",sans-serif;font-weight:500;font-size:24px;line-height:23px;margin-top:3px}
.hero-text{font-size:10.5px;line-height:14px;margin-top:8px}
.hero-more{position:absolute;left:8px;bottom:4px;font-size:8px}
.hero-photo{left:234px;top:100px;width:400px;height:235px;background:linear-gradient(90deg,#3c3a36,#8b8780 40%,#4a4a4c 75%,#2a2a2c)}

/* welcome */
.welcome-title{left:85px;top:364px;font-family:"Libre Baskerville",serif;font-size:19px;color:#111}
.welcome-title em,.section-title em{font-style:normal;color:var(--red)}
.welcome-text{left:85px;top:396px;width:370px;font-size:7.6px;line-height:13px}
.section-title{font-family:"Libre Baskerville",serif;font-size:13px;color:#111}
.services-list{left:85px;top:507px;width:160px;list-style:none;font-size:7.6px;color:var(--muted)}
.services-list li{padding:2px 0 5px;border-bottom:1px solid var(--rule);line-height:11px;margin-bottom:3px}
.services-list li:last-child{border:0}
.who-text{left:281px;top:508px;width:175px;font-size:7.6px;line-height:12px}

/* coffee form */
.coffee-form{left:476px;top:368px;width:158px;height:202px;background:var(--panel);padding:12px 11px}
.coffee-form h2{font-size:12.5px;font-weight:400;color:var(--white);margin-bottom:6px}
.coffee-form h2 b{font-weight:700}
.field{height:18px;background:var(--field);border:1px solid #4a4a4a;color:#888;font-size:7.5px;padding:4px;margin-bottom:6px}
.field-row{display:flex;gap:7px}
.field-row .field{flex:1}
.field-area{height:58px}
.submit{display:inline-block;background:var(--red);color:var(--white);font-size:7.5px;font-weight:700;padding:5px 9px;margin-top:6px}

/* divider shadow */
.shade{left:84px;top:600px;width:550px;height:14px;background:radial-gradient(ellipse at top,rgba(0,0,0,.12),transparent 70%)}

/* testimonials */
.ruled-heading{left:84px;width:550px;display:flex;align-items:center;gap:12px;justify-content:center}
.ruled-heading::before,.ruled-heading::after{content:"";flex:1;height:1px;background:var(--rule)}
.testimonial-heading{top:636px;font-family:"Libre Baskerville",serif;font-size:13px;color:#111}
.testimonial-heading em{font-style:normal;color:var(--red)}
.quote-mark{left:352px;top:662px;font-family:"Libre Baskerville",serif;font-size:22px;color:#555}
.quote-box{left:84px;top:671px;width:550px;height:70px;background:#eee;padding:12px 14px;font-family:"Libre Baskerville",serif;font-style:italic;font-size:7.4px;line-height:13px;color:#777;text-align:center}
.quote-box::after{content:"";position:absolute;left:268px;bottom:-7px;border:7px solid transparent;border-bottom:0;border-top-color:#eee}
.dots{right:86px;top:745px;display:flex;gap:3px}
.dots i{width:5px;height:5px;border-radius:50%;background:#ccc}
.dots i:first-child{background:var(--red)}
.quote-author{left:84px;top:754px;width:550px;text-align:center;font-family:"Libre Baskerville",serif;font-style:italic;font-size:7.5px;color:var(--red)}

/* partners */
.partners-heading{top:799px;font-family:"Libre Baskerville",serif;font-size:8.5px;color:var(--red);letter-spacing:.5px}
.partners{left:0;top:826px;width:719px;height:45px;background:var(--band);display:flex;justify-content:center;align-items:center;gap:38px}
.partner{background:var(--partner);opacity:.8}

/* footer */
.site-footer{left:0;top:871px;width:719px;height:329px;background:var(--charcoal);color:var(--white);text-align:center}
.social{position:absolute;top:16px;left:288px;display:flex;gap:38px}
.social i{width:22px;height:22px;border-radius:50%;background:var(--red)}
.footer-label{position:absolute;left:0;width:719px;font-family:"Libre Baskerville",serif;font-size:8.5px;letter-spacing:.4px}
.contact-col{position:absolute;top:88px;width:260px;text-align:center}
.contact-col svg{display:block;margin:0 auto 4px}
.contact-lead{font-family:"Bree Serif",serif;font-size:16px;color:var(--red);line-height:18px}
.contact-value{font-family:"Libre Baskerville",serif;font-size:16px;line-height:22px}
.footer-rule{position:absolute;left:84px;top:171px;width:550px;height:1px;background:#333}
.tweet{position:absolute;left:100px;top:216px;width:519px;font-size:8.6px;line-height:12px;color:#bbb}
.tweet b{color:var(--white);font-weight:400}
.tweet-time{position:absolute;left:0;top:244px;width:719px;font-size:7px;color:#777}
.footer-mark{position:absolute;left:349px;top:266px;width:20px;height:20px;border-radius:50%;background:var(--red)}
.footer-nav{position:absolute;left:0;top:299px;width:719px;font-size:7px;display:flex;justify-content:center;gap:14px}
.copyright{position:absolute;left:0;top:314px;width:719px;font-size:6px;color:#888}
</style>
</head>
<body>

<header class="site-header abs">
  <div class="brand abs" style="position:absolute"><span class="brand-dot"></span><span class="brand-name">Falcon IT</span></div>
  <div class="call abs">CALL US NOW ON: <strong>1300 52 64 64</strong></div>
  <div class="email-line abs">or email us at <span>support@falconit.com.au</span></div>
  <nav class="main-nav abs">
    <a href="#">HOME</a><a href="#">SERVICES</a><a href="#">PRODUCTS</a><a href="#">ABOUT</a><a href="#">DOWNLOADS</a><a href="#">CONTACT US</a>
  </nav>
</header>

<section class="hero-copy abs">
  <p class="hero-kicker">POS &amp; IT<br>SUPPORT FOR</p>
  <h1 class="hero-title">THE<br>HOSPITALITY<br>INDUSTRY</h1>
  <p class="hero-text">Lorem ipsum dolor sit amet, consectetur adipisicing elit, sed do eiusmod tempor incididunt ut labore et dolore magna aliqua.</p>
  <span class="hero-more">→&nbsp; Read more</span>
</section>
<div class="hero-photo abs" role="img" aria-label="Technician with a laptop working among server racks and network cables"></div>

<h2 class="welcome-title abs">Welcome to Falcon<em>IT</em></h2>
<p class="welcome-text abs">Lorem ipsum dolor sit amet, consectetur adipisicing elit, sed do eiusmod tempor incididunt ut labore et dolore magna aliqua. Ut enim ad minim veniam, quis nostrud exercitation ullamco laboris nisi ut aliquip ex ea commodo consequat. Duis aute irure dolor in reprehenderit in voluptate velit esse cillum dolore eu fugiat nulla pariatur. Excepteur sint occaecat cupidatat non proident, sunt in culpa qui officia deserunt mollit anim id est laborum.</p>

<h3 class="section-title abs" style="left:85px;top:484px">Our <em>Services</em></h3>
<ul class="services-list abs">
  <li>Falcon Vault Storage</li>
  <li>Reselling and supporting<br>Corvel Shieldware</li>
  <li>Trelmo Suite</li>
</ul>

<h3 class="section-title abs" style="left:281px;top:484px">Who <em>We Are</em></h3>
<p class="who-text abs">Lorem ipsum dolor sit amet, consectetur adipisicing elit, sed do eiusmod tempor incididunt ut labore et dolore magna aliqua. Ut enim ad minim veniam, quis nostrud exercitation ullamco</p>

<form class="coffee-form abs">
  <h2><b>Let's Meet</b> For Coffee!</h2>
  <div class="field">Name</div>
  <div class="field">Email</div>
  <div class="field-row"><div class="field">Company</div><div class="field">Phone</div></div>
  <div class="field field-area">Query Details</div>
  <span class="submit">SUBMIT</span>
</form>

<div class="shade abs"></div>

<h2 class="ruled-heading testimonial-heading abs">What&nbsp;<em>Our Clien's Say</em></h2>
<div class="quote-mark abs">“</div>
<blockquote class="quote-box abs">Sed ut perspiciatis unde omnis iste natus error sit voluptatem accusantium doloremque laudantium, totam rem aperiam, eaque ipsa quae ab illo inventore veritatis et quasi architecto beatae vitae dicta sunt explicabo. Nemo enim ipsam voluptatem quia voluptas sit aspernatur aut odit aut fugit, sed quia consequuntur magni dolores eos qui ratione voluptatem sequi nesciunt. Neque porro quisquam est, qui dolorem ipsum quia dolor sit amet, consectetur, adipisci velit.</blockquote>
<div class="dots abs"><i></i><i></i><i></i><i></i><i></i></div>
<p class="quote-author abs">Marla Penhaligon</p>

<h2 class="ruled-heading partners-heading abs">SUPPORTED BY</h2>
<div class="partners abs">
  <span class="partner" style="width:72px;height:12px"></span>
  <span class="partner" style="width:40px;height:24px;border-radius:3px"></span>
  <span class="partner" style="width:48px;height:16px;border-radius:4px"></span>
  <span class="partner" style="width:62px;height:12px"></span>
  <span class="partner" style="width:22px;height:22px;border-radius:50%"></span>
  <span class="partner" style="width:30px;height:26px"></span>
</div>

<footer class="site-footer abs">
  <div class="social"><i></i><i></i><i></i></div>
  <p class="footer-label" style="top:60px">HELP &amp; SUPPORT</p>

  <div class="contact-col" style="left:85px">
    <svg width="18" height="26" viewBox="0 0 18 26" aria-hidden="true"><path d="M5 2 Q1 4 1 11 Q2 20 9 24 Q12 25 14 22 L11 17 Q9 18 8 17 Q6 13 7 9 Q8 8 9 8 L8 2 Z" fill="#fff"/></svg>
    <p class="contact-lead">Need more info? Call us now!</p>
    <p class="contact-value">1300 52 64 64</p>
  </div>
  <div class="contact-col" style="left:365px">
    <svg width="26" height="20" viewBox="0 0 26 20" aria-hidden="true"><rect x="1" y="1" width="24" height="18" fill="none" stroke="#fff" stroke-width="1.6"/><path d="M1 1 L13 11 L25 1 M1 19 L10 9 M25 19 L16 9" fill="none" stroke="#fff" stroke-width="1.6"/></svg>
    <p class="contact-lead">Email</p>
    <p class="contact-value">support@falconit.com.au</p>
  </div>

  <div class="footer-rule"></div>
  <p class="footer-label" style="top:178px">FOLLOW US ON CHIRPLINE</p>
  <p class="tweet">@kestrel Proin non reos mauris, in suscipit nisl. Mauris <b>http://quorvia.co/linkpath</b> sem but I must explain to you how all this mistaken idea of denouncing</p>
  <p class="tweet-time">2 hours ago</p>
  <span class="footer-mark"></span>
  <nav class="footer-nav"><span>HOME</span><span>PRODUCTS</span><span>ABOUT</span><span>DOWNLOADS</span><span>CONTACT US</span></nav>
  <p class="copyright">© Falcon IT 2012</p>
</footer>

</body>
</html>
```